Lumvex Crating Business Card

Project Overview
We are seeking a modern, minimalist business card that effectively represents our company while making a bold and lasting impression. The design should reflect trust, professionalism, and innovation, reinforcing our expertise in custom plastic manufacturing for warehouse and distribution centers.

Provided Assets & Specifications
Logo: We will provide our official logo for integration into the design.
Design Files: Photoshop (PSD) files for our printing specifications will be supplied.

Card Size & Material:
Dimensions: 3.5" x 2"
Material: 1/8" Radius Plastic Business Cards with 1/8" Rounded Corners
Clear plastic background—the design should strategically incorporate transparency.
Orientation: The card should be designed in landscape format for a sleek and professional presentation.

Design Requirements:
Logo Prominence
The logo must be the focal point of the card.
Space should be used effectively to draw attention to the logo while maintaining a minimalist layout.

Clear Plastic Integration
The transparent background should create the illusion of blank space, enhancing the modern and high-quality feel.
Avoid any frosted effects—we do not want white areas to appear semi-transparent.

Minimalist & Impactful
Clean, structured, and easy to read at a glance.
Focus on sharp contrast to ensure legibility and visibility.
The design should instill confidence and reflect our role as a leading plastics manufacturer.

Color Palette & Contrast
Primary Colors: Blue, Black, White, and Grey
Use bold black or blue for text and key elements to ensure they stand out against the clear plastic.
Avoid light, pastel, or neon colors that may fade into the plastic background.
No frosted or semi-transparent white—we do not want a cloudy effect.

Typography & Information Hierarchy
Bold, modern typography—clear, professional, and highly legible.
The business card should highlight:
Company Logo (Primary Focus)
Full Name & Title
Phone Number
Email
Website

Brand Representation
The card should reflect our expertise in manufacturing high-quality custom plastics for large-scale packaging and distribution businesses.
Our clients rely on us to enhance their brand presence through custom plastic solutions, and our business cards should reinforce that sense of precision and trust.

Final Considerations
Utilize the clear plastic effectively to differentiate our brand from standard business cards.
Maintain a sleek, professional aesthetic while ensuring all text and elements remain legible.
The design should align with our industry, conveying reliability and innovation.
We look forward to seeing a design that captures our brand identity, maximizes the clear plastic medium, and makes a strong, professional impact on our clients.

```html
<!DOCTYPE html>
<html lang="en">
<head>
<meta charset="utf-8">
<title>Lumvex Crating Business Card</title>
<link href="https://fonts.googleapis.com/css2?family=Lato:wght@400;700;900&display=swap" rel="stylesheet">
<style>
  :root {
    --backdrop: #d9d4cc;
    --plastic: #efece7;
    --plastic-edge: #c9c3ba;
    --ink-dark: #333333;
    --ink-blue: #1d6f96;
    --ink-deep-blue: #125e95;
  }
  html, body {
    margin: 0;
    padding: 0;
    width: 1200px;
    height: 976px;
    overflow: hidden;
    background: var(--backdrop);
    font-family: "Lato", Arial, sans-serif;
  }
  .card {
    position: absolute;
    left: 180px;
    top: 248px;
    width: 840px;
    height: 480px;
    border-radius: 24px;
    background: var(--plastic);
    border: 1px solid var(--plastic-edge);
    box-sizing: border-box;
    overflow: hidden;
  }
  .brand {
    position: absolute;
    left: 40px;
    top: 62px;
    display: flex;
    align-items: center;
    gap: 14px;
  }
  .brand-square {
    width: 30px;
    height: 30px;
    background: var(--ink-deep-blue);
  }
  .brand-name {
    margin: 0;
    font-size: 46px;
    font-weight: 700;
    color: var(--ink-dark);
    line-height: 1;
    white-space: nowrap;
  }
  .feature {
    position: absolute;
    left: 429px;
    top: 12px;
    width: 397px;
    height: 442px;
    display: flex;
    flex-direction: column;
    align-items: center;
    justify-content: center;
  }
  .feature-name {
    margin: 0;
    font-size: 92px;
    font-weight: 900;
    line-height: 1.02;
    color: var(--ink-deep-blue);
    text-align: center;
  }
  .holder {
    position: absolute;
    left: 40px;
    top: 252px;
  }
  .holder-name {
    margin: 0;
    font-size: 32px;
    font-weight: 700;
    color: var(--ink-blue);
    line-height: 1.1;
    white-space: nowrap;
  }
  .holder-title {
    margin: 2px 0 0;
    font-size: 20px;
    font-weight: 400;
    color: var(--ink-dark);
  }
  .contacts {
    position: absolute;
    left: 40px;
    top: 332px;
    margin: 0;
    padding: 0;
    list-style: none;
  }
  .contacts li {
    display: flex;
    align-items: center;
    gap: 6px;
    height: 29.5px;
    font-size: 20px;
    color: var(--ink-dark);
    white-space: nowrap;
  }
  .contacts svg {
    width: 19px;
    height: 19px;
    fill: var(--ink-blue);
    flex: none;
  }
</style>
</head>
<body>
  <section class="card" aria-label="Lumvex Crating business card">
    <header class="brand">
      <span class="brand-square" aria-hidden="true"></span>
      <h1 class="brand-name">Lumvex Crating</h1>
    </header>

    <div class="feature">
      <p class="feature-name">Lumvex<br>Crating</p>
    </div>

    <div class="holder">
      <h2 class="holder-name">DORIAN KESSEL</h2>
      <p class="holder-title">President</p>
    </div>

    <ul class="contacts">
      <li>
        <svg viewBox="0 0 24 24" aria-hidden="true"><path d="M6.6 10.8a15.1 15.1 0 0 0 6.6 6.6l2.2-2.2a1 1 0 0 1 1-.25 11.4 11.4 0 0 0 3.6.57 1 1 0 0 1 1 1V20a1 1 0 0 1-1 1A17 17 0 0 1 3 4a1 1 0 0 1 1-1h3.5a1 1 0 0 1 1 1c0 1.25.2 2.45.57 3.57a1 1 0 0 1-.25 1z"/></svg>
        (905) 555-0148
      </li>
      <li>
        <svg viewBox="0 0 24 24" aria-hidden="true"><path d="M2 5h20v2l-10 6L2 7zM2 9l6 4-6 5zm20 0v9l-6-5zM9.5 14l2.5 1.5 2.5-1.5 7 5H2.5z"/></svg>
        info@lumvexcrating.com
      </li>
      <li>
        <svg viewBox="0 0 24 24" aria-hidden="true"><path d="M12 2a10 10 0 1 0 0 20 10 10 0 0 0 0-20zm6.9 6h-3a15.7 15.7 0 0 0-1.4-3.6A8 8 0 0 1 18.9 8zM12 4a14 14 0 0 1 1.9 4h-3.8A14 14 0 0 1 12 4zM4.3 14a8 8 0 0 1 0-4h3.4a16.5 16.5 0 0 0 0 4zm.8 2h3a15.7 15.7 0 0 0 1.4 3.6A8 8 0 0 1 5.1 16zm3-8h-3a8 8 0 0 1 4.4-3.6A15.7 15.7 0 0 0 8.1 8zM12 20a14 14 0 0 1-1.9-4h3.8A14 14 0 0 1 12 20zm2.3-6H9.7a14.7 14.7 0 0 1 0-4h4.6a14.7 14.7 0 0 1 0 4zm.2 5.6a15.7 15.7 0 0 0 1.4-3.6h3a8 8 0 0 1-4.4 3.6zm1.8-5.6a16.5 16.5 0 0 0 0-4h3.4a8 8 0 0 1 0 4z"/></svg>
        www.lumvexcrating.com
      </li>
    </ul>
  </section>
</body>
</html>
```